Lantern Of The Heart, Maui Ad for wellness magazine

Ad size is 7.35" x 4.625" This is 1/2 page of a magazine ad.

I titled the layout I thought best of my office as "best layout of office"

I have added 2 new pics.. please delete the older photo of my office, this one attached is photshopped, the neck is nicer on my client, and the sky is more blue.

Also, I have added a screen shot of my office photo, to show an angle that would be nice, showing the ceiling and less bare walls.

I am a Colorpuncture Therapist and an Iridologist, my practice is in Honolulu Hawaii.
This is in the category of health and wellness.

1. I have a picture that shows me giving a treatment in my office, I want the pic to be the major part of the ad. Please show ceiling tiles!! The celling with colored panels.

2. I want to show my office, and all the colors and the view from my window. This is important for what I do, and the feel for when someone comes to see me.

3. I have all the text that needs to go into the ad, my logo, and the headings completed.

Deadline is only one week! (sorry)

But I have all the necessary info completed, just need a professional clean layout.

Lastly.....

Please do not take all my screen shots i have attached for the text literally as far as color, font, size, etc, it was just easier for me to take screen shots than write it all out.
Updates

HI, I have spent all day reducing my text. I realize i was compromising the ad by wanting to say too much... I have uploaded a document with everything reduced to go on the ad... except I forgot my website on the doc.. I like the layouts already that are coming in... just with the changes of this new reduced text. www.lanternheartisle.com Thank you Tamsin

Target Market(s)

People who suffer with depression and pain

Industry/Entity Type

Health

Font styles to use
Other font styles liked:
• Overlock

Requirements
Must have
• I have updated the text so it is a shorter explanation of what I do:

Colorpuncture Therapy, colored lights focused on specific acupressure points and zones on the surface of the skin helping;
relieve anger, anxiety and depression,
restore vitality, metabolism and hormonal balance
And helps children with leaning difficulties, teeth grinding and allergies
Grand Opening Special $60 ColorTherapy Facelift, non evasive and enjoyable!

My Logo

My address is Palmetto Commerce Tower/ 2391 Banyan Blvd Ste 508, /Honolulu 96816
Across from Orchid Plaza / オーキッドプラザの向かいにあります
Phone number 808-312-4690 www.lanternheartisle.com

"Tamsin" Rosalind Farraday CCP, DIR
Certified Colorpuncturist/ Iridologist
Nice to have
• Simple, Clean, Professional, Please show the ceiling in my picture
clean, simple..
Should not have
• not too busy

```html
<!DOCTYPE html>
<html lang="en">
<head>
<meta charset="utf-8">
<title>Lantern Of The Heart, Maui — Colorpuncture Ad</title>
<link href="https://fonts.googleapis.com/css2?family=Overlock:wght@400;700;900&family=Noto+Sans+JP:wght@400&display=swap" rel="stylesheet">
<style>
  :root {
    --paper: #ffffff;
    --leaf-green: #8cc63f;
    --teal: #1aa89a;
    --teal-text: #2a7b74;
    --orange: #f7a535;
    --name-blue: #1f6fb8;
    --title-red: #e2403d;
    --ink: #4a4a4a;
    --offer-purple: #a640d8;
    --brand-teal: #1b8fa0;
  }
  * { margin: 0; padding: 0; box-sizing: border-box; }
  html, body { width: 1200px; height: 755px; overflow: hidden; background: var(--paper); }
  .ad {
    position: relative;
    width: 1200px;
    height: 755px;
    overflow: hidden;
    background: var(--paper);
    font-family: "Overlock", sans-serif;
  }
  .ad__art { position: absolute; inset: 0; }

  .brand {
    position: absolute;
    top: 88px;
    right: 16px;
    display: flex;
    align-items: center;
    gap: 8px;
    font-weight: 700;
    font-size: 19px;
    color: var(--brand-teal);
  }
  .brand__dot { width: 12px; height: 12px; border-radius: 50%; background: var(--brand-teal); }

  .practitioner {
    position: absolute;
    left: 18px;
    top: 554px;
    width: 420px;
    text-align: center;
  }
  .practitioner__name {
    font-weight: 700;
    font-size: 21px;
    line-height: 26px;
    letter-spacing: 0.3px;
    color: var(--name-blue);
    text-transform: uppercase;
  }
  .practitioner__role {
    font-size: 16px;
    line-height: 20px;
    color: var(--title-red);
  }
  .practitioner__address {
    margin-top: 24px;
    font-style: normal;
    font-size: 14px;
    line-height: 19px;
    color: var(--ink);
  }
  .practitioner__address .jp { font-family: "Noto Sans JP", sans-serif; font-size: 13px; }
  .practitioner__contact {
    margin-top: 18px;
    font-size: 14px;
    line-height: 18px;
    color: var(--ink);
  }

  .about {
    position: absolute;
    left: 493px;
    top: 553px;
    width: 700px;
    font-size: 14.5px;
    line-height: 18px;
    color: var(--teal-text);
  }
  .about p + p { margin-top: 16px; }

  .offer {
    position: absolute;
    left: 490px;
    top: 687px;
  }
  .offer__headline {
    font-size: 33px;
    line-height: 32px;
    color: var(--offer-purple);
    text-transform: uppercase;
    white-space: nowrap;
  }
  .offer__detail {
    font-size: 22.5px;
    line-height: 22px;
    color: var(--teal-text);
    white-space: nowrap;
  }
</style>
</head>
<body>
<main class="ad">
  <svg class="ad__art" width="1200" height="755" viewBox="0 0 1200 755">
    <defs>
      <linearGradient id="wash-left" x1="0" y1="0" x2="0.6" y2="1">
        <stop offset="0" stop-color="#d8efae"/>
        <stop offset="1" stop-color="#ffffff" stop-opacity="0"/>
      </linearGradient>
      <linearGradient id="wash-right" x1="1" y1="0" x2="0" y2="1">
        <stop offset="0" stop-color="#d5efa6"/>
        <stop offset="0.6" stop-color="#eef8dc"/>
        <stop offset="1" stop-color="#ffffff"/>
      </linearGradient>
      <linearGradient id="photo-tones" x1="0" y1="0" x2="0" y2="1">
        <stop offset="0" stop-color="#a9d8ee"/>
        <stop offset="0.3" stop-color="#6fa95a"/>
        <stop offset="0.42" stop-color="#d6e6e2"/>
        <stop offset="0.6" stop-color="#9cc7c4"/>
        <stop offset="0.85" stop-color="#b9d3d0"/>
        <stop offset="1" stop-color="#e9eeee"/>
      </linearGradient>
    </defs>

    <path class="wash wash--left" d="M0 300 L0 560 Q200 520 460 520 L0 300 Z" fill="url(#wash-left)"/>
    <path class="wash wash--right" d="M1200 300 L1200 755 L520 755 Q700 560 1200 300 Z" fill="url(#wash-right)"/>

    <path role="img" aria-label="Photo: the therapist giving a colorpuncture light treatment to a client lying on a table, in a bright office with a window view of palm trees and blue sky"
          d="M0 68 Q540 -40 1120 82 Q1170 94 1200 110 L1200 360 Q860 560 300 446 Q120 410 0 366 Z"
          fill="url(#photo-tones)"/>

    <path class="curve curve--green" d="M0 70 Q540 -30 1060 40" fill="none" stroke="var(--leaf-green)" stroke-width="9" stroke-linecap="round"/>
    <path class="curve curve--orange" d="M0 474 Q260 440 560 526 Q300 462 0 492 Z" fill="var(--orange)"/>
    <path class="curve curve--teal" d="M300 446 Q860 560 1200 360 L1200 372 Q860 580 300 446 Z" fill="var(--teal)"/>
    <path class="curve curve--leaf" d="M1010 420 Q1120 400 1200 340 L1200 352 Q1120 414 1010 420 Z" fill="var(--leaf-green)"/>
  </svg>

  <div class="brand">
    <span class="brand__dot"></span>
    <span class="brand__name">Lantern Of The Heart, Maui</span>
  </div>

  <section class="practitioner">
    <h1 class="practitioner__name">“Tamsin” Rosalind Farraday CCP, DIR</h1>
    <p class="practitioner__role">Colorpuncture Therapist/ Iridologist</p>
    <address class="practitioner__address">
      Palmetto Commerce Tower<br>
      2391 Banyan Blvd Ste 508, Honolulu, Hi 96816<br>
      Across from Orchid Plaza<br>
      <span class="jp">オーキッドプラザの向かいにあります</span>
    </address>
    <p class="practitioner__contact">808-312-4690 &nbsp;| &nbsp;www.lanternheartisle.com</p>
  </section>

  <section class="about">
    <p>Colorpuncture Therapy relieves physical pain, anxiety, depression, anger and helps restore hormonal balance.<br>
    We become happier, peaceful, find purpose, direction and reconnect with the the Self.</p>
    <p>In Colorpuncture Therapy frequencies of colored light are focused on the skin using a hand held light tool, as the<br>
    light is absorbed by the skin, it stimulates intra-cellular communication which supports healing.</p>
    <p>Colorpuncture is gentle, relaxing and non-evasive</p>
  </section>

  <section class="offer">
    <h2 class="offer__headline">Grand Opening Special $60</h2>
    <p class="offer__detail">ColorTherapy Facelift, gentle and non-evasive</p>
  </section>
</main>
</body>
</html>
```